Advertisement Coaching practice

I need an advertisement (to be printed in newspaper). I have a coaching practice where I offer coaching, workshops family constellations and relationship therapy. The ad needs to express calmness, inspiration to transform but also not dull and boring. It would be great if you could use the colors from my logo into the ad.

Dimensions are: 13,04 cm Width x 9,72 cm Height.

I will add my previous self-made ad, my company logo, a portrait photo of myself and the text I want to add. Also my contact details should be visible as well.

Requirements
Nice to have
• I have updated the brief with a flyer that I had previously made by a designer. It would be a nice to have if the ad ties in with that. You can also look at my website at www.fernbrook.nu to see what colors I used there.

```html
<!DOCTYPE html>
<html lang="nl">
<head>
<meta charset="utf-8">
<title>Advertentie coachingpraktijk</title>
<link rel="stylesheet" href="https://fonts.googleapis.com/css2?family=Montserrat:wght@800&family=Roboto:wght@400;500;700&display=swap">
<style>
  :root{
    --stage:#3a3a3a;
    --ink:#555557;
    --band-grey:#58595b;
    --mint:#88cdb3;
    --mint-light:#d9efe6;
    --paper:#f6f9f8;
    --teal:#25919a;
    --white:#ffffff;
  }
  *{box-sizing:border-box;margin:0;padding:0}
  html,body{width:1200px;height:1200px;overflow:hidden;background:var(--stage)}
  body{position:relative;font-family:"Roboto",Arial,sans-serif}
  .ad{
    position:absolute;left:43px;top:165px;width:1114px;height:843px;overflow:hidden;
    background:linear-gradient(100deg,var(--mint-light) 0%,var(--paper) 75%,#fafcfb 100%);
    box-shadow:0 4px 14px rgba(0,0,0,.35);
  }
  .ad-shapes{position:absolute;left:0;top:0}
  .headline{
    position:absolute;left:55px;top:44px;
    font-family:"Montserrat",Arial,sans-serif;font-weight:800;
    font-size:47px;line-height:52px;color:var(--ink);letter-spacing:.2px;
  }
  .brand{position:absolute;left:820px;top:50px;width:240px;text-align:center}
  .brand-dot{display:block;margin:0 auto 18px;width:68px;height:68px;border-radius:50%;border:2px solid #8e8e8e}
  .brand-name{font-family:"Roboto",Arial,sans-serif;font-weight:400;font-size:40px;color:var(--ink);letter-spacing:1px}
  .intro{
    position:absolute;left:55px;top:257px;width:1010px;
    color:var(--white);font-size:23.5px;line-height:34px;
  }
  .intro strong{font-weight:700}
  .offer-title{
    position:absolute;left:55px;top:340px;
    color:var(--white);font-weight:700;font-size:31px;line-height:42px;
  }
  .benefits{position:absolute;left:52px;top:396px;list-style:none}
  .benefit{position:relative;padding-left:67px;color:var(--ink);font-size:24.5px;line-height:31px;margin-bottom:14px;width:700px}
  .benefit-icon{position:absolute;left:0;top:2px;width:40px;height:40px}
  .portrait{
    position:absolute;left:768px;top:303px;width:320px;height:320px;border-radius:50%;
    border:3px solid #5a5a5c;
    background:radial-gradient(circle at 50% 40%,#9a6a52 0%,#6b4a3c 35%,#b9c3d3 70%,#e9eef2 100%);
  }
  .about{
    position:absolute;left:55px;top:624px;width:672px;
    color:var(--white);font-size:21.5px;line-height:34.4px;text-align:justify;
  }
  .divider{position:absolute;left:777px;top:633px;width:3px;height:153px;background:var(--white)}
  .contact{position:absolute;left:822px;top:632px;color:var(--white)}
  .contact-name{font-weight:700;font-size:27px;line-height:36px;margin-bottom:6px}
  .contact-line{display:flex;align-items:center;font-size:22px;line-height:40px}
  .contact-line svg{width:26px;height:26px;margin-right:17px;flex:none}
</style>
</head>
<body>
<main class="ad">
  <svg class="ad-shapes" width="1114" height="843" viewBox="0 0 1114 843" aria-hidden="true">
    <rect x="0" y="247" width="1114" height="87" fill="var(--band-grey)"/>
    <rect x="0" y="334" width="1114" height="54" fill="var(--mint)"/>
    <path d="M0,515 Q330,610 790,590 Q360,606 0,548 Z" fill="var(--band-grey)"/>
    <path d="M0,556 Q520,665 1114,528 L1114,843 L0,843 Z" fill="var(--teal)"/>
    <path d="M0,550 Q380,622 790,593" fill="none" stroke="#f1f7f5" stroke-width="3"/>
  </svg>

  <h1 class="headline">COACHING-<br>FAMILIEOPSTELLINGEN &amp;<br>RELATIETHERAPIE</h1>

  <div class="brand">
    <span class="brand-dot"></span>
    <span class="brand-name">fernbrook</span>
  </div>

  <p class="intro"><strong>Trauma's en negatieve ervaringen</strong> vormen ons en blijven nog lang voelbaar. Ze kunnen groei of geluk in de weg staan.</p>

  <h2 class="offer-title">Ik ben Mirela en ondersteun je bij het:</h2>

  <ul class="benefits">
    <li class="benefit">
      <svg class="benefit-icon" viewBox="0 0 40 40" aria-hidden="true"><circle cx="20" cy="20" r="18.5" fill="none" stroke="#555" stroke-width="2"/><rect x="10" y="15" width="20" height="7" fill="none" stroke="#555" stroke-width="2"/><path d="M13 22v8M27 22v8M13 15v-4M27 15v-4" stroke="#555" stroke-width="2"/></svg>
      Doorbreken van belemmerende patronen
    </li>
    <li class="benefit">
      <svg class="benefit-icon" viewBox="0 0 40 40" aria-hidden="true"><circle cx="20" cy="20" r="18.5" fill="none" stroke="#555" stroke-width="2"/><path d="M13 30v-6a8 8 0 1 1 13 -6l2 4h-3v4h-4v4" fill="none" stroke="#555" stroke-width="2"/></svg>
      Beter omgaan met conflicten
    </li>
    <li class="benefit">
      <svg class="benefit-icon" viewBox="0 0 40 40" aria-hidden="true"><circle cx="20" cy="20" r="18.5" fill="none" stroke="#555" stroke-width="2"/><path d="M9 16h14M17 26h14" stroke="#555" stroke-width="2"/><circle cx="20" cy="21" r="2.5" fill="none" stroke="#555" stroke-width="1.6"/></svg>
      In gezonde verbinding met elkaar als koppel of met anderen komen
    </li>
  </ul>

  <div class="portrait" role="img" aria-label="Portretfoto van de coach"></div>

  <p class="about">Maandelijks geef ik workshops familieopstellingen. Ook houd ik themasessies rond adoptie, moeder-dochterdynamiek of relaties. Ook bied ik individuele coaching, relatietherapie en retraites aan. Kijk op de website voor meer info of neem contact op en ontdek wat het beste bij jou past.</p>

  <div class="divider"></div>

  <address class="contact" style="font-style:normal">
    <div class="contact-name">Mirela Santos</div>
    <div class="contact-line">
      <svg viewBox="0 0 26 26" aria-hidden="true"><rect x="2" y="5" width="22" height="16" fill="none" stroke="#fff" stroke-width="2"/><path d="M2 5l11 9 11-9M2 21l8-8M24 21l-8-8" fill="none" stroke="#fff" stroke-width="2"/></svg>
      info@fernbrook.nu
    </div>
    <div class="contact-line">
      <svg viewBox="0 0 26 26" aria-hidden="true"><path d="M6 3l4 5-2 3c1 3 4 6 7 7l3-2 5 4-3 4C12 23 3 14 2 6z" fill="none" stroke="#fff" stroke-width="2" stroke-linejoin="round"/></svg>
      06-12 34 56 78
    </div>
    <div class="contact-line">
      <svg viewBox="0 0 26 26" aria-hidden="true"><circle cx="13" cy="13" r="11" fill="none" stroke="#fff" stroke-width="2"/><ellipse cx="13" cy="13" rx="5" ry="11" fill="none" stroke="#fff" stroke-width="2"/><path d="M2 13h22M4 7h18M4 19h18" stroke="#fff" stroke-width="1.6"/></svg>
      www.fernbrook.nu
    </div>
  </address>
</main>
</body>
</html>
```